Designing promotion page - poster for Folk High School

I would like a attractive and well-designed page /poster used in a catalogue for the Tavelund Learning Colleges.
The dimensions on the graphical element:
Width: 180 mm
Hight:186 mm
Resolution: min. 450 dpi
This graphical element will be combined with other information about the school, that is static and we cannot change. Please see attachment (“Folk High School – placement of graphic”). The almost square area in the middle of the page iss the one that the designed grapichal element will fill.
A part of completing this, is to hand over the workfile to us in the end when we choose the design (Adobe Photoshop PSD or an InDesign INDD file must be used)
There are also attached some pictures that you are free to use in creating the design as you like. You will choose how many pictures you want to use. Please cut, scale, adjust and sharpen them as you like. Only one requirement: Please use one of the Sri Lanka pictures.
Be creative.
The following text-elements must be used in the page (They are also prioritized – number one means: most important that the reader reads…)
1. Møtet som forandrer --- headline. Yep; needs a font supporting ÆØÅ...
2. Multisport --- different courses we provide at our school.
- Data Media – Japan
- Barn i Fokus
- Helse og Velvære
- Globalt Fokus – Afrika
- Fotball
- Bil og Motor
- Internasjonal
- Worship – Australia
- KISS-friluft
- Høy Puls
Alle linjer reiser på egne turer i inn –og utland! ---- This should be included as the different courses, but in the bottum of the «box».
3. Spennende fellestur for alle til Sri Lanka ---- Use together with the picture from Sri Lanke (Not too large picture!)
4. Hva skal du bli? ---- small headline.
Vi er gode på veiledning, og hjelper deg med å finne ut hva du skal bli.
5. Flott skole:
- Basseng
- Styrkerom
- Gymsal
- Internatstuer
- Filmsal
- Skolekjøkken
- Verksted
- Fotostudio
- Fitnessrom
_________
The students attending our school is between 18-20 years. Of course, the design and expression must meet their expectations.
Looking forward to see the first drafts!
To understand what this should look like: Check the following link:
https://leafrack.net/tavelundskolen/docs/tlc_guide__18__web
The poster / graphic we want to create, is similar to the one you find in this brochure from page 20.

```html
<!DOCTYPE html>
<html lang="no">
<head>
<meta charset="utf-8">
<title>Møtet som forandrer – Tavelund Learning Colleges</title>
<link rel="stylesheet" href="https://fonts.googleapis.com/css2?family=Oswald:wght@300;400;500;600&display=swap">
<style>
  :root {
    --red: #ef4a45;
    --red-deep: #8e2a2a;
    --ink: #0d0d0d;
    --paper: #ffffff;
    --orange: #e8652f;
    --orange-soft: #f3a06b;
    --wine: #6b2020;
    --blush: #f5c9c2;
  }
  * { margin: 0; padding: 0; box-sizing: border-box; }
  html, body { width: 1161px; height: 1200px; overflow: hidden; background: var(--paper); }
  .poster {
    position: relative; width: 1161px; height: 1200px; overflow: hidden;
    background: var(--paper); font-family: "Oswald", sans-serif; color: var(--ink);
  }
  .artwork { position: absolute; inset: 0; }
  .hexagon { filter: drop-shadow(4px 10px 12px rgba(0,0,0,.28)); }
  .headline {
    position: absolute; left: 266px; width: 624px; text-align: center;
    color: var(--red); font-weight: 400; font-size: 84px; line-height: 1;
    letter-spacing: 15px; text-indent: 15px;
  }
  .headline--top { top: 410px; }
  .headline--bottom { top: 504px; }
  .courses {
    position: absolute; left: 266px; width: 624px; top: 588px; text-align: center;
    color: var(--paper); font-weight: 300; font-size: 20px; line-height: 28.5px; letter-spacing: 2.4px;
  }
  .courses .sep { color: var(--red); padding: 0 4px; }
  .guidance-title {
    position: absolute; top: 925px; left: 0; width: 1161px; text-align: center;
    font-weight: 300; font-size: 36px; letter-spacing: 6px;
  }
  .guidance-text {
    position: absolute; top: 970px; left: 0; width: 1161px; text-align: center;
    font-weight: 300; font-size: 18px; letter-spacing: 2.6px;
  }
  .divider { position: absolute; top: 1009px; left: 169px; width: 847px; height: 1px; background: var(--red); }
  .facilities {
    position: absolute; top: 1024px; left: 175px; width: 830px; text-align: center;
    font-weight: 300; font-size: 17px; line-height: 23px; letter-spacing: 2.4px;
  }
  .facilities strong { font-weight: 600; }
  .trip-band {
    position: absolute; left: 0; top: 1100px; width: 1161px; height: 100px;
    background: var(--red); color: var(--paper); text-align: center;
    font-weight: 500; font-size: 24px; letter-spacing: 5.5px; line-height: 34px; padding-top: 14px;
  }
</style>
</head>
<body>
<main class="poster">
  <svg class="artwork" width="1161" height="1200" viewBox="0 0 1161 1200" aria-hidden="false">
    <defs>
      <linearGradient id="sunsetTone" x1="0" y1="1" x2="1" y2="0">
        <stop offset="0" stop-color="#d9452f"/><stop offset=".5" stop-color="#e8652f"/><stop offset="1" stop-color="#f3a06b"/>
      </linearGradient>
      <linearGradient id="islandTone" x1="0" y1="0" x2="0" y2="1">
        <stop offset="0" stop-color="#c24444"/><stop offset="1" stop-color="#7a2424"/>
      </linearGradient>
      <linearGradient id="campfireTone" x1="0" y1="0" x2="0" y2="1">
        <stop offset="0" stop-color="#9c3a3a"/><stop offset=".55" stop-color="#4a1818"/><stop offset="1" stop-color="#2c0f0f"/>
      </linearGradient>
      <linearGradient id="friendsTone" x1="0" y1="0" x2="1" y2="1">
        <stop offset="0" stop-color="#b8673e"/><stop offset="1" stop-color="#e0a070"/>
      </linearGradient>
      <linearGradient id="jumpTone" x1="0" y1="0" x2="1" y2="0">
        <stop offset="0" stop-color="#f0b7ae"/><stop offset="1" stop-color="#fbe3de"/>
      </linearGradient>
    </defs>

    <g class="brush brush--left">
      <polygon role="img" aria-label="Solnedgang over havet" fill="url(#sunsetTone)"
        points="70,385 200,300 330,250 470,140 555,62 500,160 430,230 320,380 270,450 160,520 60,560 120,470"/>
      <polygon role="img" aria-label="Fiskere på påler ved kysten av Sri Lanka" fill="url(#islandTone)"
        points="0,610 120,540 240,470 330,440 390,500 360,700 330,820 240,880 120,950 0,1000"/>
      <polygon fill="#e8652f" points="230,250 330,200 300,240"/>
      <polygon fill="#c24444" points="20,560 90,520 60,580"/>
      <polygon fill="#e8652f" points="400,160 470,110 440,170"/>
    </g>

    <g class="brush brush--right">
      <polygon role="img" aria-label="Elever rundt leirbål ved en innsjø" fill="url(#campfireTone)"
        points="680,250 830,170 960,110 1161,20 1161,330 1000,400 900,430 860,390"/>
      <polygon role="img" aria-label="To venninner med solbriller" fill="url(#friendsTone)"
        points="880,470 1000,420 1161,345 1161,405 1060,480 960,540 880,590"/>
      <polygon role="img" aria-label="Elever som hopper på stranden" fill="url(#jumpTone)"
        points="890,630 1000,570 1161,470 1161,630 1080,680 960,720 900,705"/>
      <polygon fill="#9c3a3a" points="1040,60 1120,25 1090,70"/>
      <polygon fill="#e0a070" points="1100,420 1161,395 1140,430"/>
    </g>

    <polygon class="hexagon" fill="var(--ink)"
      points="578,189 890,368 890,728 578,907 266,728 266,368"/>
  </svg>

  <h1 class="headline headline--top">MØTET SOM</h1>
  <h1 class="headline headline--bottom">FORANDRER</h1>

  <p class="courses">
    VÅRE LINJER<span class="sep">|</span>DATA MEDIA – JAPAN<span class="sep">|</span>BARN I FOKUS<br>
    HELSE OG VELVÆRE<span class="sep">|</span>GLOBALT FOKUS – AFRIKA<br>
    FOTBALL<span class="sep">|</span>BIL OG MOTOR<span class="sep">|</span>INTERNASJONAL<br>
    WORSHIP – AUSTRALIA<span class="sep">|</span>KISS-FRILUFT<span class="sep">|</span>HØY PULS
  </p>

  <h2 class="guidance-title">HVA SKAL DU BLI?</h2>
  <p class="guidance-text">VI ER GODE PÅ VEILEDNING, OG HJELPER DEG MED Å FINNE UT HVA DU SKAL BLI.</p>
  <div class="divider"></div>
  <p class="facilities"><strong>FLOTT SKOLE:</strong>BASSENG-STYRKEROM-GYMSAL-INTERNATSTUER-FILMSAL-SKOLEK-<br>JØKEN-VERKSTED-FOTOSTUDIO-FITNESSROM</p>

  <footer class="trip-band">
    ALLE LINJER REISER PÅ EGNE TURER I INN –OG UTLAND!<br>
    SPENNENDE FELLESTUR FOR ALLE TIL SRI LANKA
  </footer>
</main>
</body>
</html>
```